Need Wordpress business website designed for the website Quarrowden.com

Quarrowden.com needs a Wordpress website to connect mineral rights buyers and sellers from across the United States. This website will be a userfriendly listing service. Below is a list of requirements that need to be accomplished for this project.
-Logo design
-5 to 10 pages of SEO content with copy included. 100-200 words per page.
-Responsive Web design.
-User-friendly add listing page and view listing pages. (2 out of the 7-10 pages needed)
1. Home page
This will have short introduction and possible video plugin.
Welcome to QuarRowden.com. Market your minerals to a large group of investors. By marketing your mineral rights on QuarRowden.com Investors compete so you get a fair market offer.
Contact: 844-317-2906
info@Quarrowden.com
2. Our Service or About us Page
-Get the best price for your mineral rights and oil and gas royalties
-Market your mineral rights to attract the best price possible
-Connect you to reputable mineral rights buyers
-Help you understand the industry and answer all of your questions
Our representatives are here to answer any questions you may have.
3 Add Listing Page
Add listing page will need the following boxes
First Name:
Last Name:
Phone Number:
Email:
State:
County:
Net Acres:
Price Per Acre:
Leased Producing
Legal Description:
Comments:
4 View Listing Page
View listing Page will need the following info:
First Name:
Last Name:
Phone Number:
Email:
State:
County:
Net Acres:
Price Per Acre:
Leased Producing
Legal Description:
Comments:
View listings page will need the following:
Listing Number
State: Insert drop down box or fill in form
County: Insert drop down box or fill in form
Legal Description: Fill in form
Net Acres: Fill in form
Price: Fill in form
Notes:
Date Listed:
Interested in this listing? Call 844-317-2906 or fill out the contact box below.
Contact Box:
First Name
Last Name
Email
Phone Number
Questions/Comments?
5. Why Sell?
Receive an immediate lump sum cash payment now.
-Minimize your risk. Protect yourself from the uncertainties of the industry. (Falling natural gas prices, Shut-in and poor producing wells, Infrastructure and pipeline delays)
-Lower taxes. Your mineral rights sale will be taxed at 20% while royalty and bonus payments are taxed as ordinary income at 35%
-Estate Planning. Eliminate complicated forms such as maintenance and depletion schedules, division order agreements, and 1099’s.
-Diversify your assets while paying down bad debt
-Utilize the 1031 tax exchange to invest in more property tax free.
6. News
Page with news articles.
-Research on most important Keywords needed for site.
-Implementation of meta data and HTML elements of site.
-Implement robot tags where needed.
- Creation of sitemap and submission to search engines.
Google Analytics
-Intall a website traffic statistics program that provides important information about viewership. Need to track daily visitors, top search engines and referral sites, bounce rate, top landing pages, mobile traffic, etc...
Google webmaster tools
-Install webmaster tools to determine health and technical status of website.
Listing distribution service
-website needs listed with all four major listing data providers. Brindlet, Vorthel, pallowset, and Kembrite.
Video Plugin
-Option to include video greeting and instruction on homepage.
Setup of Social Media Accounts
-Google+, Facebook, and Linkedin Account pages.
Example Webpages:
holdfieldtrader.com
tandrocksbourse.com
grauvenlandings.com
bidtallowcrestlots.com
Target Market(s)
Mineral Rights Owners, Landowners, Mineral Rights Buyers, Oil and Gas Owners, Oil and Gas buyers, Oil and Gas Royalty Owners, Oil and Gas Royalty Buyers, Oil and Gas investors, Mineral Rights Investors.
Industry/Entity Type
Oil And Gas
Font styles to use
Requirements
Must have
- -contact box on the right side
- -Location information on bottom of site.
- -live chat box plugin
- -listing box with the following drop down boxes
- First Name:
- Last Name:
- Phone Number:
- Email:
- State:
- County:
- Net Acres:
- Price Per Acre:
- Leased? Producing?
- Legal Description:
- Comments:
Nice to have
- Video plugin on Home page

```html
<!DOCTYPE html>
<html lang="en">
<head>
<meta charset="utf-8">
<title>Quarrowden.com — Mineral Rights Listings</title>
<link rel="stylesheet" href="https://fonts.googleapis.com/css2?family=Aldrich&family=Arimo:wght@400;700&family=Open+Sans:wght@300;400;600;700&display=swap">
<style>
:root{
  --orange:#f26a10;
  --black:#000;
  --dark:#1c1c1c;
  --footer:#1a1a1a;
  --grey-band:#e4e4e4;
  --text:#555;
  --text-dark:#222;
  --muted:#888;
  --link:#3a8fc6;
  --white:#fff;
}
*{margin:0;padding:0;box-sizing:border-box}
html,body{width:1200px;height:2243px;overflow:hidden;background:var(--black)}
body{font-family:"Arimo",Arial,sans-serif;position:relative}
.abs{position:absolute}

/* header */
.site-header{position:absolute;left:0;top:0;width:1200px;height:105px;background:var(--black)}
.brand{position:absolute;left:82px;top:26px;display:flex;align-items:center;gap:12px}
.brand-mark{width:30px;height:30px;background:var(--orange)}
.brand-name{font-family:"Arimo",sans-serif;font-weight:700;font-size:25px;color:var(--white);line-height:1.05;width:240px}
.phone{position:absolute;left:618px;top:12px;display:flex;align-items:center;gap:10px;color:var(--white);font-size:25px;font-family:"Arimo",sans-serif}
.search{position:absolute;left:861px;top:10px;width:254px;height:37px;border:2px solid var(--orange);color:var(--white);font-size:13px;padding:9px 10px}
.search svg{position:absolute;right:8px;top:9px}
.main-nav{position:absolute;top:66px;left:0;width:1200px;height:24px}
.main-nav a{position:absolute;color:var(--white);text-decoration:none;font-family:"Open Sans",sans-serif;font-size:16px;font-weight:600}

/* hero */
.hero{position:absolute;left:0;top:105px;width:1200px;height:484px;
  background:linear-gradient(180deg,#4f7fae 0%,#9ab7d0 35%,#c9d6dd 50%,#7d9a66 62%,#4d7d2e 80%,#2f5f1c 100%)}
.play{position:absolute;left:565px;top:203px}

/* welcome */
.welcome{position:absolute;left:0;top:589px;width:1200px;height:416px;background:var(--white);text-align:center}
.welcome h1{position:absolute;top:31px;width:100%;font-family:"Open Sans",sans-serif;font-weight:400;font-size:27px;color:var(--text);letter-spacing:.5px}
.welcome p{position:absolute;left:150px;width:900px;font-size:13px;color:var(--muted);line-height:20px}
.btn-outline{position:absolute;left:494px;top:177px;width:152px;height:45px;border:2px solid var(--orange);font-family:"Open Sans",sans-serif;font-size:13px;color:var(--text-dark);line-height:41px}
.feature{position:absolute;top:268px;width:260px;text-align:center}
.feature h3{font-family:"Open Sans",sans-serif;font-weight:400;font-size:17px;color:var(--text);margin-top:10px}
.feature h3 b{font-weight:700;color:var(--text-dark)}
.feature p{font-size:11px;color:var(--muted);line-height:14px;margin:6px auto 0;width:220px}

/* video band */
.video-band{position:absolute;left:0;top:1005px;width:1200px;height:475px;background:var(--dark)}
.monitor{position:absolute;left:87px;top:38px;width:512px;height:304px;background:#0b0b0b;border:3px solid #3a3a3a;border-radius:8px}
.monitor-screen{position:absolute;left:22px;top:19px;width:449px;height:257px;
  background:linear-gradient(180deg,#3d4a5a 0%,#8a7b6a 45%,#d88a3a 62%,#6b4a2a 78%,#1c1510 100%)}
.monitor-chin{position:absolute;left:87px;top:342px;width:512px;height:33px;background:linear-gradient(#e9e9e9,#bdbdbd);border-radius:0 0 8px 8px}
.monitor-stand{position:absolute;left:298px;top:375px;width:90px;height:50px;background:linear-gradient(90deg,#9a9a9a,#dcdcdc,#9a9a9a)}
.monitor-base{position:absolute;left:258px;top:423px;width:170px;height:14px;background:#cfcfcf;border-radius:50%}
.watch-btn{position:absolute;left:257px;top:163px;width:155px;height:50px;background:var(--orange);border-radius:25px;color:var(--white);font-family:"Open Sans",sans-serif;font-size:16px;display:flex;align-items:center;gap:8px;padding-left:8px}
.video-copy{position:absolute;left:621px;top:72px;width:555px}
.video-copy h2{font-family:"Aldrich",sans-serif;font-weight:400;font-size:20px;color:var(--white);letter-spacing:.5px}
.video-copy p{margin-top:16px;font-size:12.4px;line-height:22.5px;color:var(--white)}
.read-more{display:block;margin-top:12px;font-size:13px;color:var(--orange);text-decoration:none}

/* cards */
.cards{position:absolute;left:0;top:1480px;width:1200px;height:449px;background:var(--grey-band)}
.cards h2{position:absolute;top:33px;width:100%;text-align:center;font-size:19px;font-weight:700;color:var(--text-dark)}
.card{position:absolute;top:77px;width:239px;height:309px;text-align:center}
.card.is-active{background:var(--white)}
.card-photo{width:155px;height:155px;border-radius:50%;margin:0 auto;margin-top:0}
.card h3{font-family:"Open Sans",sans-serif;font-weight:600;font-size:15px;color:#333;margin-top:26px}
.card p{font-size:11.5px;color:#555;line-height:14px;width:190px;margin:10px auto 0}
.card a{display:block;margin-top:12px;font-size:11.5px;color:var(--link);text-decoration:none;font-weight:700}

/* footer */
.site-footer{position:absolute;left:0;top:1929px;width:1200px;height:212px;background:var(--footer)}
.footer-col{position:absolute;top:44px;color:var(--white)}
.footer-col h4{font-family:"Aldrich",sans-serif;font-weight:400;font-size:23px;margin-bottom:14px}
.footer-col p,.footer-col li{font-size:11.5px;line-height:22.5px;list-style:none}
.news-input{position:absolute;left:3px;top:48px;width:229px;height:32px;background:var(--white)}
.news-btn{position:absolute;left:235px;top:48px;width:122px;height:32px;background:#333;color:var(--white);font-size:11px;font-weight:700;text-align:center;line-height:32px}

.bottom-bar{position:absolute;left:0;top:2141px;width:1200px;height:55px;background:var(--orange)}
.copyright{position:absolute;left:87px;top:21px;font-size:10px;color:var(--white)}
.social{position:absolute;top:16px;width:23px;height:23px;border-radius:50%;background:var(--white)}

.chat{position:absolute;left:816px;top:2196px;width:384px;height:47px;background:var(--black);border-top:1px solid #333;display:flex;align-items:center;padding-left:22px;gap:22px;color:var(--white);font-size:11.5px;font-weight:700}
.chat-toggle{position:absolute;right:12px;bottom:6px;width:14px;height:12px;border:1.5px solid var(--white)}
</style>
</head>
<body>

<header class="site-header">
  <div class="brand">
    <div class="brand-mark"></div>
    <div class="brand-name">Quarrowden Marketplace</div>
  </div>
  <div class="phone">
    <svg width="26" height="26" viewBox="0 0 26 26"><circle cx="13" cy="13" r="12" fill="none" stroke="var(--orange)" stroke-width="2"/><path d="M9 7c1 0 2 2 2.4 3 .2.6-1 1.4-1 1.8.5 1.4 1.8 2.8 3.2 3.4.4.1 1.2-1.2 1.8-1 1 .4 3 1.4 3 2.4 0 1-1.4 2.2-2.4 2.2C11 18.8 7.2 15 7 9.4 7 8.4 8 7 9 7z" fill="var(--orange)"/></svg>
    01 2345 6789
  </div>
  <div class="search">Search
    <svg width="16" height="16" viewBox="0 0 16 16"><circle cx="6.5" cy="6.5" r="4.5" fill="none" stroke="var(--orange)" stroke-width="2"/><line x1="10" y1="10" x2="14.5" y2="14.5" stroke="var(--orange)" stroke-width="2"/></svg>
  </div>
  <nav class="main-nav">
    <a style="left:434px">Home</a>
    <a style="left:520px">Our Services</a>
    <a style="left:668px">Add Listing</a>
    <a style="left:804px">View Listing</a>
    <a style="left:946px">Why Sell?</a>
    <a style="left:1068px">News</a>
  </nav>
</header>

<section class="hero" role="img" aria-label="Video greeting: presenter in a suit standing before green rolling hills under a cloudy blue sky">
  <svg class="play" width="72" height="72" viewBox="0 0 72 72"><circle cx="36" cy="36" r="36" fill="#000"/><path d="M29 23l21 13-21 13z" fill="#fff"/></svg>
</section>

<section class="welcome">
  <h1>WELCOME TO QUARROWDEN.COM</h1>
  <p style="top:76px">Welcome to QuarRowden.com. Our service has helped many Mineral Owners get top dollar by putting their mineral rights in front of our large market of Mineral rights Buyers and Investors. Click on the Add Listing button below to get started.</p>
  <p style="top:132px">To receive a direct offer from us on your mineral rights or oil and gas royalties, please fill out the form below. A representative will be in touch to discuss an offer.</p>
  <div class="btn-outline">ADD LISTING</div>

  <div class="feature" style="left:127px">
    <svg width="44" height="44" viewBox="0 0 44 44"><circle cx="22" cy="20" r="17" fill="none" stroke="#222" stroke-width="2.5"/><circle cx="22" cy="20" r="11" fill="#222"/><text x="22" y="25" text-anchor="middle" font-size="14" font-weight="700" fill="#fff" font-family="Arimo,sans-serif">$</text><path d="M10 32l-3 10 6-3 3 5 3-9M34 32l3 10-6-3-3 5-3-9" fill="#222"/></svg>
    <h3>Get the <b>Best price</b></h3>
    <p>Lorem Ipsum is simply dummy text of the printing and typesetting of the industry. Lorem Ipsum has been</p>
  </div>
  <div class="feature" style="left:471px">
    <svg width="44" height="44" viewBox="0 0 44 44"><circle cx="22" cy="13" r="9" fill="#222"/><path d="M6 43c0-11 7-18 16-18s16 7 16 18z" fill="#222"/><path d="M20 26l2 10 2-10z" fill="#fff"/></svg>
    <h3>Connect you to <b>Rights Buyers</b></h3>
    <p>Lorem Ipsum is simply dummy text of the printing and typesetting of the industry. Lorem Ipsum has been</p>
  </div>
  <div class="feature" style="left:818px">
    <svg width="50" height="44" viewBox="0 0 50 44"><path d="M3 8h15l4 5h25v27H3z" fill="none" stroke="#222" stroke-width="2.5"/><path d="M3 40l6-20h39l-6 20" fill="none" stroke="#222" stroke-width="2.5"/></svg>
    <h3><b>Lorem Ipsum</b> is simply</h3>
    <p>Lorem Ipsum is simply dummy text of the printing and typesetting of the industry. Lorem Ipsum has been</p>
  </div>
</section>

<section class="video-band">
  <div class="monitor">
    <div class="monitor-screen" role="img" aria-label="Oil pump jack silhouetted against a sunset sky"></div>
  </div>
  <div class="monitor-chin"></div>
  <div class="monitor-stand"></div>
  <div class="monitor-base"></div>
  <div class="watch-btn">
    <svg width="34" height="34" viewBox="0 0 34 34"><circle cx="17" cy="17" r="16" fill="#fff"/><path d="M13 10l11 7-11 7z" fill="var(--orange)"/></svg>
    Watch Video
  </div>
  <div class="video-copy">
    <h2>Lorem Ipsum is simply dummy text of the</h2>
    <p>Lorem Ipsum is simply dummy text of the printing and typesetting industry. Lorem Ipsum has been the industry's standard dummy text ever since the 1500s, when an unknown printer took a galley of type and scrambled it to make a type specimen book. It has survived not only five centuries, but also the leap into electronic typesetting, remaining essentially unchanged. It was popularised in the 1960s with the release of Lettrafil sheets containing Lorem Ipsum passages, and more recently with desktop publishing software like Calden PageForm including versions of Lorem Ipsum.</p>
    <a class="read-more">READ MORE</a>
  </div>
</section>

<section class="cards">
  <h2>Lorem Ipsum is simply dummy text of the printing</h2>
  <article class="card is-active" style="left:85px">
    <div class="card-photo" role="img" aria-label="Pump jack on a green field under a pale blue sky" style="background:linear-gradient(180deg,#9cc0de 0%,#c8dced 55%,#4f7a2c 62%,#2e5518 100%)"></div>
    <h3>Lorem Ipsum is</h3>
    <p>Lorem Ipsum is simply dummy text of the printing and typesetting industry. Lorem Ipsum has</p>
    <a>Read More</a>
  </article>
  <article class="card" style="left:350px">
    <div class="card-photo" role="img" aria-label="Open green farmland under a blue sky with clouds" style="background:linear-gradient(180deg,#3f7fc4 0%,#a8c8e6 48%,#7fae3a 58%,#4d8a1e 100%)"></div>
    <h3>Lorem Ipsum is</h3>
    <p>Lorem Ipsum is simply dummy text of the printing and typesetting industry. Lorem Ipsum has</p>
    <a>Read More</a>
  </article>
  <article class="card" style="left:605px">
    <div class="card-photo" role="img" aria-label="Pump jack silhouetted against an orange sunset" style="background:linear-gradient(180deg,#4a4a52 0%,#b07a4a 40%,#e8a04a 58%,#5a3a20 75%,#1a120c 100%)"></div>
    <h3>Lorem Ipsum is</h3>
    <p>Lorem Ipsum is simply dummy text of the printing and typesetting industry. Lorem Ipsum has</p>
    <a>Read More</a>
  </article>
  <article class="card" style="left:869px">
    <div class="card-photo" role="img" aria-label="Green meadow with trees under a cloudy sky" style="background:linear-gradient(180deg,#6e8ea8 0%,#c6d3dc 45%,#5d8a3a 58%,#36621e 100%)"></div>
    <h3>Lorem Ipsum is</h3>
    <p>Lorem Ipsum is simply dummy text of the printing and typesetting industry. Lorem Ipsum has</p>
    <a>Read More</a>
  </article>
</section>

<footer class="site-footer">
  <div class="footer-col" style="left:87px">
    <h4>Contact Us</h4>
    <p>QuarRowden.com</p>
    <p>2914 Halvern Road NW #208</p>
    <p>Canton, Ohio 44720</p>
  </div>
  <div class="footer-col" style="left:312px">
    <h4>Quick Link</h4>
    <ul><li>Privacy Policy</li><li>Sitemap</li><li>Contact info</li></ul>
  </div>
  <div class="footer-col" style="left:494px;width:220px">
    <h4>About Us</h4>
    <p>Lorem Ipsum is simply dummy text of the printing and typesetting industry. Lorem Ipsum has been the industry's</p>
  </div>
  <div class="footer-col" style="left:758px;width:360px">
    <h4>Newsletter</h4>
    <div class="news-input"></div>
    <div class="news-btn">SUBSCRIBE</div>
  </div>
</footer>

<div class="bottom-bar">
  <p class="copyright">COPYRIGHT 2015 QUARROWDEN.COM ALL RIGHTS RESERVED</p>
  <span class="social" style="left:994px"></span>
  <span class="social" style="left:1032px"></span>
  <span class="social" style="left:1069px"></span>
  <span class="social" style="left:1107px"></span>
</div>

<div class="chat">
  <svg width="32" height="28" viewBox="0 0 32 28"><path d="M2 2h28v18H12l-7 6v-6H2z" fill="none" stroke="#fff" stroke-width="2.5"/><line x1="8" y1="8" x2="24" y2="8" stroke="#fff" stroke-width="2"/><line x1="8" y1="13" x2="20" y2="13" stroke="#fff" stroke-width="2"/></svg>
  Welcome To Quarrowden Marketplace
  <span class="chat-toggle"></span>
</div>

</body>
</html>
```